Start-up consultancy in Healthcare Space requiring clean and crisp website design

I am the founder of a start-up consultancy to improve access to medicines and healthcare around the globe. My primary product are consulting services to both the public sector and the private sector to work on: improved healthcare delivery, the right price for medicines and addressing challenges in emerging markets. As the sector is fairly conservative, I need a clean and very professional website as is should signal competence in the sector. Therefore, I like shades of white and green but there should be a link to healthcare. Please see the logo that is featured on my business cards.

Target Market(s)

Ministry of Health, Pharmaceutical companies, Emerging Markets (Latin America, Middle East, Eastern Europe, Asia)

Industry/Entity Type

Healthcare

Coding

Coded - Design and coding required

Number of Pages Required

5+ page

Font styles to use
Serif

Colors

Designer to choose colors to be used in the design.

Requirements
Must have
• About Section
• Services Section
• Blog Section
• The website design should also portray the solution for access to healthcare and highlight my ability to help clients with that.
• The website will be hosted on a CMS and should therefore be easy to adjust. I would prefer wordpress but open to any suggestions as I have my own webspace.
• I quite like these websites:
• https://www.velmiracare.com/why-velmira
• https://home.tanquilwellness.com/
Nice to have
• I like to see some creative thinking with the theme of healthcare.
Should not have
• The design should not feature too many hospitals or pills etc. as this is really not my focus.

```html
<!DOCTYPE html>
<html lang="en">
<head>
<meta charset="utf-8">
<title>Veranth Consulting</title>
<link href="https://fonts.googleapis.com/css2?family=Open+Sans:wght@300;400;600;700&display=swap" rel="stylesheet">
<style>
:root{
  --green:#0b6b3a;
  --green-dark:#07552d;
  --green-soft:#9fbfa8;
  --ink:#333;
  --muted:#777;
  --line:#e4e4e4;
  --band:#f4f4f4;
  --footer:#222;
  --footer-deep:#161616;
  --white:#fff;
}
*{box-sizing:border-box;margin:0;padding:0}
html,body{width:1200px;height:2416px;overflow:hidden}
body{font-family:"Open Sans",Arial,sans-serif;color:var(--ink);background:var(--white);position:relative}
.site-header{position:absolute;top:0;left:0;width:1200px;height:72px;background:var(--white);z-index:2;border-bottom:1px solid var(--line)}
.brand{position:absolute;left:120px;top:8px;display:flex;align-items:center;gap:10px;background:var(--white);padding:14px 22px;border-radius:0 0 40px 40px}
.brand-mark{width:22px;height:22px;border-radius:50%;background:var(--green)}
.brand-name{font-size:19px;font-weight:600;color:var(--green);letter-spacing:1px}
.main-nav{position:absolute;right:80px;top:0;height:72px;display:flex;align-items:center;gap:36px}
.main-nav a{font-size:12px;font-weight:600;color:#555;text-decoration:none;letter-spacing:.5px;padding:26px 0}
.main-nav a.active{color:var(--green);border-bottom:2px solid var(--green)}
.search-btn{width:30px;height:30px;border:1px solid #ccc;border-radius:50%;display:flex;align-items:center;justify-content:center}
.hero{position:absolute;top:72px;left:0;width:1200px;height:508px;background:linear-gradient(100deg,#c9dcd3 0%,#e7efec 45%,#f6f3f1 75%,#e9e1dc 100%)}
.hero-dots{position:absolute;left:80px;bottom:18px;display:flex;gap:6px}
.hero-dots span{width:9px;height:9px;border-radius:50%;background:#fff;opacity:.7}
.hero-dots span.on{background:var(--green);opacity:1}
.section-title{text-align:center;font-weight:300;font-size:30px;letter-spacing:1px;color:#444;text-transform:uppercase}
.section-title.green{color:var(--green)}
.section-sub{text-align:center;font-size:12px;color:var(--muted);margin-top:10px}
.welcome{position:absolute;top:600px;left:0;width:1200px;height:280px;text-align:center}
.welcome .section-title{margin-top:16px}
.welcome-lead{margin-top:12px;font-size:13px;font-weight:600;color:var(--green);letter-spacing:.5px}
.welcome-text{width:760px;margin:16px auto 0;font-size:12.5px;line-height:22px;color:var(--muted)}
.btn{display:inline-block;background:var(--green);color:#fff;font-size:12px;font-weight:700;letter-spacing:1px;padding:11px 24px;border-radius:3px;margin-top:24px}
.services{position:absolute;top:880px;left:0;width:1200px;height:500px;background:var(--band);border-top:1px solid var(--line);padding-top:40px}
.service-row{display:flex;justify-content:center;gap:70px;margin-top:40px}
.service{width:270px;text-align:center}
.service-circle{width:200px;height:200px;margin:0 auto;border-radius:50%;background:#fff;box-shadow:0 0 0 1px #e6e6e6;display:flex;flex-direction:column;align-items:center;justify-content:center;gap:16px}
.service-circle.featured{background:var(--green)}
.service-label{font-size:14px;color:#666;letter-spacing:.5px}
.featured .service-label{color:#fff}
.service-text{margin-top:40px;font-size:12px;line-height:21px;color:var(--muted)}
.blog{position:absolute;top:1380px;left:0;width:1200px;height:580px;padding-top:28px}
.blog-grid{position:absolute;top:120px;left:88px;width:1024px;display:grid;grid-template-columns:repeat(3,1fr);gap:10px}
.blog-col{display:flex;flex-direction:column}
.post-text{height:200px;border:1px solid var(--line);padding:28px 26px;text-align:center}
.post-title{font-size:13px;font-weight:600;color:#444}
.post-body{margin-top:14px;font-size:12px;line-height:21px;color:var(--muted)}
.post-bar{height:36px;background:var(--green);color:#fff;font-size:11px;font-weight:600;display:flex;justify-content:space-between;align-items:center;padding:0 22px}
.post-bar span{display:flex;align-items:center;gap:6px}
.post-photo{height:200px}
.cta{position:absolute;top:1960px;left:0;width:1200px;height:220px;background:var(--green);text-align:center;color:#fff;padding-top:44px}
.cta h2{font-weight:300;font-size:30px;letter-spacing:1px}
.cta p{width:620px;margin:14px auto 0;font-size:12.5px;line-height:21px;color:#d9e9df}
.btn-outline{display:inline-block;border:1px solid #fff;color:#fff;font-size:11px;font-weight:700;letter-spacing:1px;padding:10px 20px;margin-top:20px}
.site-footer{position:absolute;top:2180px;left:0;width:1200px;height:180px;background:var(--footer);color:#bbb;font-size:12px}
.footer-col{position:absolute;top:28px}
.footer-col h3{font-size:14px;font-weight:600;color:#fff;letter-spacing:1px;margin-bottom:14px}
.footer-col p{line-height:21px}
.newsletter-form{display:flex;margin-top:2px}
.newsletter-form .field{width:210px;height:36px;background:#fff;color:#999;font-size:12px;padding:10px 12px}
.newsletter-form .submit{height:36px;background:var(--green);color:#fff;font-size:11px;font-weight:700;padding:11px 16px}
.social{display:flex;gap:10px}
.social span{width:34px;height:34px;border-radius:50%;border:1px solid #fff}
.copyright{position:absolute;top:2360px;left:0;width:1200px;height:56px;background:var(--footer-deep);color:#999;font-size:12px;text-align:center;line-height:56px}
</style>
</head>
<body>
<header class="site-header">
  <div class="brand"><span class="brand-mark"></span><span class="brand-name">VERANTH CONSULTING</span></div>
  <nav class="main-nav">
    <a class="active">HOME</a><a>ABOUT US</a><a>SERVICES</a><a>BLOG</a><a>CONTACT US</a>
    <span class="search-btn"><svg width="13" height="13" viewBox="0 0 14 14"><circle cx="6" cy="6" r="4.5" fill="none" stroke="#555" stroke-width="1.6"/><line x1="9.3" y1="9.3" x2="13" y2="13" stroke="#555" stroke-width="1.6"/></svg></span>
  </nav>
</header>

<section class="hero" role="img" aria-label="Doctor with stethoscope beside floating healthcare icons for health, accessibility and medical care">
  <div class="hero-dots"><span class="on"></span><span></span><span></span></div>
</section>

<section class="welcome">
  <h1 class="section-title">Welcome to Veranth Consulting</h1>
  <p class="welcome-lead">SED UT PERSPICIATIS UNDE OMNIS ISTE NATUS ERROR SIT VOLUPTATEM ACCUSANTIUM</p>
  <p class="welcome-text">We help ministries of health, pharmaceutical companies and partners in emerging markets widen access to medicines and care. Our team brings field experience in pricing, delivery systems and market entry, turning complex health challenges into clear, workable plans that reach more patients and strengthen local health systems over the long term.</p>
  <span class="btn">READ MORE</span>
</section>

<section class="services">
  <h2 class="section-title green">Our Services</h2>
  <p class="section-sub">Practical advice for public and private clients working to improve access to healthcare.</p>
  <div class="service-row">
    <div class="service">
      <div class="service-circle">
        <span class="service-label">CONSULTANCY</span>
        <svg width="56" height="44" viewBox="0 0 56 44" fill="#8a8a8a"><circle cx="14" cy="8" r="6"/><circle cx="42" cy="8" r="6"/><rect x="6" y="16" width="16" height="18" rx="3"/><rect x="34" y="16" width="16" height="18" rx="3"/><rect x="18" y="26" width="20" height="4"/><rect x="26" y="30" width="4" height="12"/></svg>
      </div>
      <p class="service-text">Strategy and policy support for ministries and companies shaping better healthcare delivery in growing markets.</p>
    </div>
    <div class="service">
      <div class="service-circle featured">
        <span class="service-label">MEDICINES</span>
        <svg width="60" height="44" viewBox="0 0 60 44"><g transform="rotate(-35 18 24)"><rect x="4" y="16" width="30" height="14" rx="7" fill="#fff"/><rect x="19" y="16" width="15" height="14" rx="0" fill="#cfe3d6"/></g><circle cx="46" cy="30" r="10" fill="#fff"/><line x1="38" y1="30" x2="54" y2="30" stroke="#0b6b3a" stroke-width="2"/></svg>
      </div>
      <p class="service-text">Pricing and access models that set the right price for medicines and keep supply steady for patients.</p>
    </div>
    <div class="service">
      <div class="service-circle">
        <span class="service-label">HEALTHCARE</span>
        <svg width="52" height="44" viewBox="0 0 52 44" fill="#8a8a8a"><rect x="22" y="2" width="10" height="26"/><rect x="14" y="10" width="26" height="10"/><path d="M2 34 q10-8 20-2 h12 q4 0 4 4 h-14 M2 42 h30 l16-10 q-4-4-8-1 l-8 5"/></svg>
      </div>
      <p class="service-text">Field insight on the real challenges of care in Latin America, the Middle East, Europe and Asia.</p>
    </div>
  </div>
</section>

<section class="blog">
  <h2 class="section-title green">Latest Blog</h2>
  <p class="section-sub">Notes and insight from our work on medicines, pricing and health systems.</p>
  <div class="blog-grid">
    <article class="blog-col">
      <div class="post-text"><h3 class="post-title">SED UT PERSPICIATIS UNDE</h3><p class="post-body">How emerging markets can close the gap in medicine access with smarter pricing and local partners.</p></div>
      <div class="post-bar"><span>▣ 14 MAY 2017</span><span>✎ COMMENTS</span></div>
      <div class="post-photo" role="img" aria-label="Desk with glasses, notebook and papers" style="background:linear-gradient(135deg,#ded4c4,#b9a98f)"></div>
    </article>
    <article class="blog-col">
      <div class="post-photo" role="img" aria-label="Medicine bottles and capsules on a table" style="background:linear-gradient(135deg,#c9d6e2,#8fa9c2)"></div>
      <div class="post-bar"><span>▣ 14 MAY 2017</span><span>✎ COMMENTS</span></div>
      <div class="post-text"><h3 class="post-title">SED UT PERSPICIATIS UNDE</h3><p class="post-body">How emerging markets can close the gap in medicine access with smarter pricing and local partners.</p></div>
    </article>
    <article class="blog-col">
      <div class="post-text"><h3 class="post-title">SED UT PERSPICIATIS UNDE</h3><p class="post-body">How emerging markets can close the gap in medicine access with smarter pricing and local partners.</p></div>
      <div class="post-bar"><span>▣ 14 MAY 2017</span><span>✎ COMMENTS</span></div>
      <div class="post-photo" role="img" aria-label="Doctor talking with a patient in a bright clinic" style="background:linear-gradient(135deg,#f1ece8,#d8c8be)"></div>
    </article>
  </div>
</section>

<section class="cta">
  <h2>LET'S GET STARTED</h2>
  <p>Ready to improve access to healthcare for the people you serve? Talk to our team about a plan that fits your market and goals.</p>
  <span class="btn-outline">CLICK HERE FOR MORE INFO</span>
</section>

<footer class="site-footer">
  <div class="footer-col" style="left:80px">
    <h3>CONTACT US</h3>
    <p>Level 4, 210 Harbour Street,<br>Sydney NSW 2000</p>
  </div>
  <div class="footer-col" style="left:320px;top:62px">
    <p>Phone : +(000) 123-4567<br>Email : info@veranthconsulting.com</p>
  </div>
  <div class="footer-col" style="left:620px">
    <h3>NEWSLETTER</h3>
    <div class="newsletter-form"><span class="field">Email</span><span class="submit">SUBSCRIBE</span></div>
  </div>
  <div class="footer-col" style="left:980px">
    <h3>FOLLOW US</h3>
    <div class="social"><span></span><span></span><span></span></div>
  </div>
</footer>
<div class="copyright">Copyright © 2017 Veranth Consulting. All rights reserved</div>
</body>
</html>
```